Website Design - for Energy Efficiency company - large corporate feel

Hi there,
Thanks for checking out this project!
We're a UK based energy efficiency business. We arrange for energy efficient systems to be fitted in people's houses (i.e. efficient boilers, solar panels etc.) However, we do not install them ourselves as we have accredited installers who install on our behalf. Therefore the website should appeal to these businesses and have a very professional corporate feel. The final design should communicate that we are a financially safe large corporation.
Our existing website should not be used for inspiration as the style and content are very outdated (it was from a time when were installers - which we no longer are).
The new website design should use the greens from our logo, however I don't want the site saturated in this colour.
I'm really open to your chosen layout and therefore I'm not a huge fan of including links to websites I like - as I don't want to limit your own creativity. However, I would like it to look corporate (but not too boring and unimaginative).
So here's a few links to websites that I feel give a feel of financially safe / large corporate etc. Although you certainly don't have to design with this style / layout in mind:
http://www.brelvanhub.org.uk/advice
http://www.tolvenrise.co.uk/
http://www.qpwd.org.uk/
http://www.wendrowkeyplot.co.uk/
http://www.ruvasto.co.uk/ (very bad design but looks corporate)
http://www.pellarwatt.org.uk/
http://www.vq.co.uk/ (looks corporate but too busy and boring)
http://www.quellisto.co.uk/business/index.htm
http://www.dormavel.com/
https://www.ostrevan.com/en/index.html
The site is for 4 different audiences:
Consumers | Businesses | Public Sector | Installers
Therefore, it's important that there is some form of way of splitting the site up into these sections (almost like 4 websites in 1). Each section will then have the navigation menu with 7 links.
I've attached our logo (company-logo.jpg) and another logo design we have to display inline with regulations (blue-pact-logo.jpg).
Happy designing, and thank you!

```html
<!DOCTYPE html>
<html lang="en">
<head>
<meta charset="utf-8">
<title>Verdanel Energy – Home</title>
<link rel="stylesheet" href="https://fonts.googleapis.com/css2?family=Arimo:wght@400;700&display=swap">
<style>
  :root {
    --page-bg: #f4f5f5;
    --band-grey: #e8ebec;
    --white: #ffffff;
    --green-brand: #5b9a1f;
    --green-bright: #9aca12;
    --green-light: #8cc63f;
    --green-dark: #548527;
    --green-fold: #6e9a2c;
    --charcoal: #424242;
    --text-dark: #222222;
    --text-mid: #666666;
    --text-soft: #888888;
  }
  * { box-sizing: border-box; margin: 0; padding: 0; }
  html, body { width: 1200px; height: 1000px; overflow: hidden; }
  body {
    position: relative;
    background: var(--page-bg);
    font-family: "Arimo", Arial, sans-serif;
    color: var(--text-mid);
  }
  .abs { position: absolute; }

  /* Header */
  .topbar { left: 0; top: 0; width: 1200px; height: 77px; background: var(--white); }
  .lang-switch { right: 222px; top: 7px; font-size: 9px; color: var(--text-mid); word-spacing: 2px; }
  .navband { left: 0; top: 77px; width: 1200px; height: 54px; background: var(--band-grey); }
  .brand { left: 246px; top: 64px; display: flex; align-items: center; gap: 8px; text-decoration: none; }
  .brand-dot { width: 20px; height: 20px; border-radius: 50%; background: var(--green-brand); }
  .brand-name { font-size: 21px; font-weight: 700; color: var(--green-brand); letter-spacing: -0.3px; }
  .main-nav { left: 545px; top: 77px; width: 433px; display: flex; justify-content: space-between; height: 54px; }
  .main-nav a {
    display: block; padding: 23px 0 0; font-size: 10px;
    color: var(--text-mid); text-decoration: none; white-space: nowrap;
  }
  .main-nav a.active { color: var(--green-brand); border-top: 3px solid var(--green-light); padding: 20px 13px 0; }

  /* Hero slider */
  .hero { left: 246px; top: 138px; width: 732px; height: 324px; }
  .hero svg { display: block; }
  .caption-left {
    left: 221px; top: 359px; width: 414px; height: 53px; background: rgba(140,198,63,0.88);
    padding: 13px 0 0 34px; color: var(--white); font-size: 13px; line-height: 17px;
  }
  .caption-right {
    left: 578px; top: 387px; width: 424px; height: 62px; background: rgba(140,198,63,0.9);
    display: flex; align-items: center; padding-left: 62px;
  }
  .caption-right h2 { font-size: 20px; font-weight: 400; color: var(--text-dark); margin-right: 16px; white-space: nowrap; }
  .caption-right p { font-size: 9px; line-height: 11px; color: #3c6a12; width: 190px; }
  .slider-dots { left: 589px; top: 473px; display: flex; gap: 3px; }
  .slider-dots span { width: 8px; height: 7px; background: #cfcfcf; }
  .slider-dots span.current { background: #8a8a8a; }

  /* Audience cards */
  .card { padding: 22px 0 0 23px; }
  .card h3 { font-size: 13px; font-weight: 400; margin-bottom: 12px; }
  .card .lede { font-size: 10px; color: var(--green-brand); margin-bottom: 12px; }
  .card .body { font-size: 7.5px; line-height: 10px; width: 260px; }
  .card .more { position: absolute; left: 23px; font-size: 9px; text-decoration: underline; }
  .card-consumers { left: 244px; top: 490px; width: 361px; height: 177px; background: var(--white); border: 1px solid var(--green-light); }
  .card-consumers h3 { color: var(--text-mid); }
  .card-consumers .body { color: var(--text-soft); }
  .card-consumers .more { top: 125px; color: var(--green-light); }
  .card-business { left: 612px; top: 490px; width: 366px; height: 177px; background: var(--green-bright); padding-left: 27px; overflow: hidden; }
  .card-business h3 { color: var(--white); margin-bottom: 28px; }
  .card-business .body { color: #3d5a06; }
  .card-business .more { left: 27px; top: 125px; color: var(--text-dark); }
  .card-business .clock { position: absolute; left: 9px; top: 97px; }
  .card-public { left: 244px; top: 674px; width: 361px; height: 177px; background: var(--charcoal); border-bottom: 2px solid var(--green-light); }
  .card-public h3 { color: var(--white); }
  .card-public .photo {
    position: absolute; left: 24px; top: 50px; width: 107px; height: 78px;
    background: #1e1e1e; padding: 5px;
  }
  .card-public .photo div { width: 100%; height: 100%; background: linear-gradient(135deg, #9dbb8f, #d8dfe2 55%, #6b7d88); }
  .card-public .body { position: absolute; left: 153px; top: 52px; width: 190px; color: #cfcfcf; }
  .card-public .body p + p { margin-top: 10px; }
  .card-public .more { top: 134px; color: var(--green-light); }
  .card-installers { left: 612px; top: 674px; width: 366px; height: 177px; background: var(--green-dark); padding-left: 27px; }
  .card-installers h3 { color: var(--white); margin-bottom: 28px; }
  .card-installers .body { color: #162a05; }
  .card-installers .more { left: 27px; top: 133px; color: var(--text-dark); }

  /* Footer */
  .footer-links { left: 0; top: 857px; width: 1200px; height: 40px; background: var(--white); }
  .footer-links ul { position: absolute; left: 244px; top: 18px; list-style: none; display: flex; font-size: 7px; color: var(--text-soft); white-space: nowrap; }
  .footer-links li + li::before { content: "|"; margin: 0 8px; }
  .follow { position: absolute; left: 860px; top: 12px; display: flex; align-items: center; gap: 8px; font-size: 12px; color: var(--text-mid); }
  .follow span.social { width: 21px; height: 21px; border-radius: 50%; background: #707070; }
  .follow span.social:first-of-type { margin-left: 12px; }
  .footer-base { left: 0; top: 897px; width: 1200px; height: 103px; background: var(--band-grey); }
  .copyright { left: 245px; top: 933px; font-size: 7.5px; color: var(--green-brand); }
  .divider { left: 375px; top: 920px; width: 1px; height: 52px; background: #d3d7d9; }
  .footer-brand { left: 404px; top: 937px; font-size: 14px; font-weight: 700; color: var(--green-brand); white-space: nowrap; }
  .badge { left: 562px; top: 918px; width: 44px; height: 50px; background: var(--green-dark); }
</style>
</head>
<body>
  <header>
    <div class="abs topbar"></div>
    <div class="abs lang-switch">English &nbsp;|&nbsp; Language</div>
    <div class="abs navband"></div>
    <a class="abs brand" href="#">
      <span class="brand-dot"></span><span class="brand-name">VERDANEL ENERGY</span>
    </a>
    <nav class="abs main-nav">
      <a class="active" href="#">Home</a>
      <a href="#">About Us</a>
      <a href="#">Blue Pact</a>
      <a href="#">ECO</a>
      <a href="#">Landlords</a>
      <a href="#">Renewables</a>
      <a href="#">Contact Us</a>
    </nav>
  </header>

  <section class="abs hero">
    <svg width="732" height="324" viewBox="0 0 732 324">
      <defs>
        <linearGradient id="heroLeft" x1="0" y1="0" x2="0.8" y2="1">
          <stop offset="0" stop-color="#8dbdf0"/>
          <stop offset="0.3" stop-color="#3b5fa0"/>
          <stop offset="0.75" stop-color="#26457e"/>
          <stop offset="1" stop-color="#c9ced4"/>
        </linearGradient>
        <linearGradient id="heroRight" x1="0" y1="0" x2="0" y2="1">
          <stop offset="0" stop-color="#2a5db5"/>
          <stop offset="0.35" stop-color="#3a6fc6"/>
          <stop offset="0.7" stop-color="#3d4350"/>
          <stop offset="1" stop-color="#4a80d0"/>
        </linearGradient>
      </defs>
      <polygon role="img" aria-label="Photo of rooftop solar panel array under a blue sky" points="0,0 554,0 318,324 0,324" fill="url(#heroLeft)"/>
      <polygon role="img" aria-label="Photo of a pole-mounted solar panel against a deep blue sky" points="566,0 732,0 732,324 330,324" fill="url(#heroRight)"/>
      <polygon points="554,0 566,0 330,324 318,324" fill="#ffffff"/>
    </svg>
  </section>
  <svg class="abs" style="left:221px;top:341px" width="26" height="19" aria-hidden="true"><polygon points="25,0 25,18 0,18" fill="var(--green-fold)"/></svg>
  <div class="abs caption-left">Lorem ipsum dolor sit amet, consectetur adipisicing elit,<br>sed do eiusmod</div>
  <div class="abs caption-right">
    <h2>Solar Panels</h2>
    <p>Lorem ipsum dolor sit amet, consectetur adipisicing elit, sed do eiusmod</p>
  </div>
  <svg class="abs" style="left:978px;top:449px" width="25" height="14" aria-hidden="true"><polygon points="0,0 24,0 0,13" fill="var(--green-fold)"/></svg>
  <div class="abs slider-dots"><span class="current"></span><span></span><span></span><span></span></div>

  <main>
    <article class="abs card card-consumers">
      <h3>Consumers</h3>
      <p class="lede">Lorem ipsum dolor sit amet, consectetur</p>
      <p class="body">Lorem ipsum dolor sit amet, consectetur adipisicing elit, sed do eiusmod tempor incididunt ut labore et dolore magna aliqua.</p>
      <a class="more" href="#">Read More &gt;&gt;</a>
    </article>
    <article class="abs card card-business">
      <svg class="clock" width="100" height="100" viewBox="0 0 100 100" aria-hidden="true">
        <circle cx="50" cy="50" r="44" fill="none" stroke="rgba(255,255,255,0.3)" stroke-width="5"/>
        <polyline points="50,18 50,52 30,72" fill="none" stroke="rgba(255,255,255,0.3)" stroke-width="5"/>
      </svg>
      <h3>Businesses</h3>
      <p class="body">Lorem ipsum dolor sit amet, consectetur adipisicing elit, sed do eiusmod tempor incididunt ut labore et dolore magna aliqua.</p>
      <a class="more" href="#">Read More &gt;&gt;</a>
    </article>
    <article class="abs card card-public">
      <h3>Public Sector</h3>
      <div class="photo"><div role="img" aria-label="Photo of a businesswoman standing by an office window"></div></div>
      <div class="body">
        <p>Lorem ipsum dolor sit amet, consectetur adipisicing elit, sed do eiusmod tempor incididunt ut labore et dolore magna aliqua.</p>
        <p>Lorem ipsum dolor sit amet, consectetur adipisicing elit, sed do eiusmod tempor incididunt ut labore et dolore magna aliqua.</p>
      </div>
      <a class="more" href="#">Read More &gt;&gt;</a>
    </article>
    <article class="abs card card-installers">
      <h3>Installers</h3>
      <p class="body">Lorem ipsum dolor sit amet, consectetur adipisicing elit, sed do eiusmod tempor incididunt ut labore et dolore magna aliqua.</p>
      <a class="more" href="#">Read More &gt;&gt;</a>
    </article>
  </main>

  <footer>
    <div class="abs footer-links">
      <ul>
        <li>Lorem ipsum dolor</li><li>Lorem dolor</li><li>Lorem ipsum dolor</li><li>Lorem ipsum</li><li>Lorem ipsum dolor</li><li>Lorem m dolor</li><li>Lorem sum dolor</li>
      </ul>
      <div class="follow">Follow Us <span class="social"></span><span class="social"></span></div>
    </div>
    <div class="abs footer-base"></div>
    <div class="abs copyright">© &nbsp;2013. All Right Reserved</div>
    <div class="abs divider"></div>
    <div class="abs footer-brand">VERDANEL ENERGY</div>
    <div class="abs badge" role="img" aria-label="Approved provider badge"></div>
  </footer>
</body>
</html>
```